Casino with the 'highest winning percentage' needs a stationery design

This is for a casino in Colombo, Sri Lanka and we need a stationery design for business card, letter head and envelope.

Should be very professional, simple and elegant without fancy fonts

Reason: Not fully satisfied with the designs. Need more designs.

Industry/Entity Type

Business

Requirements
Must have
• 1. card deck symbol 'CLUBS' in red, or black

2. name in BLOCK CAPITAL LETTERS

3. Preferred font colours are black, white or red

4. Prefer 'professional /elegant' fonts
Should not have
• SHOULD NOT HAVE ANY OTHER SYMBOL EXCEPT 'CLUBS'

DO NOT PREFER ITALIC FONTS

```html
<!DOCTYPE html>
<html lang="en">
<head>
<meta charset="utf-8">
<title>Corvane Entertainment – Business Card</title>
<link rel="stylesheet" href="https://fonts.googleapis.com/css2?family=Questrial&display=swap">
<style>
  :root {
    --page-bg: #e4e4e4;
    --card-white: #f7f7f7;
    --card-black: #1f1f1f;
    --brand-red: #d0161b;
    --ink: #1c1c1c;
    --band-dark: #262626;
  }
  * { box-sizing: border-box; margin: 0; padding: 0; }
  html, body {
    width: 1200px;
    height: 900px;
    overflow: hidden;
  }
  body {
    background: var(--page-bg);
    font-family: "Questrial", sans-serif;
    color: var(--ink);
    position: relative;
  }
  .card {
    position: absolute;
    left: 260px;
    width: 680px;
    height: 390px;
    box-shadow: 0 6px 18px rgba(0,0,0,0.18);
  }
  /* Back of card */
  .card-back {
    top: 40px;
    background: var(--card-black);
    display: flex;
    align-items: center;
    justify-content: center;
  }
  .card-back .brand-name {
    color: var(--brand-red);
    font-size: 34px;
    letter-spacing: 3px;
  }
  /* Front of card */
  .card-front {
    top: 470px;
    background: var(--card-white);
  }
  .brand-lockup {
    position: absolute;
    left: 262px;
    top: 62px;
    display: flex;
    align-items: center;
    gap: 20px;
  }
  .brand-dot {
    width: 50px;
    height: 50px;
    border-radius: 50%;
    background: var(--brand-red);
    flex: none;
  }
  .brand-name-stack {
    color: var(--ink);
    font-size: 29px;
    line-height: 1.02;
    letter-spacing: 1.5px;
  }
  .contact-list {
    position: absolute;
    right: 356px;
    top: 216px;
    list-style: none;
    font-size: 15.5px;
    line-height: 21px;
  }
  .contact-list li {
    display: flex;
    justify-content: flex-end;
    align-items: center;
    gap: 14px;
  }
  .contact-icon {
    width: 12px;
    height: 12px;
    fill: var(--brand-red);
    flex: none;
  }
  .company-address {
    position: absolute;
    left: 345px;
    top: 237px;
    font-style: normal;
    font-size: 15.5px;
    line-height: 21px;
  }
  .company-web {
    color: var(--brand-red);
    font-size: 16px;
    letter-spacing: 0.5px;
  }
  .footer-band {
    position: absolute;
    left: 0;
    right: 0;
    bottom: 14px;
    height: 13px;
    display: flex;
    gap: 6px;
  }
  .footer-band .band-red { flex: 0 0 48%; background: var(--brand-red); }
  .footer-band .band-dark { flex: 1; background: var(--band-dark); }
</style>
</head>
<body>

  <section class="card card-back" aria-label="Business card, back">
    <span class="brand-name">CORVANE</span>
  </section>

  <section class="card card-front" aria-label="Business card, front">
    <div class="brand-lockup">
      <span class="brand-dot"></span>
      <div class="brand-name-stack">
        CORVANE<br>ENTERTAINMENT<br>SRI LANKA
      </div>
    </div>

    <ul class="contact-list">
      <li>+ 94 11 5550182
        <svg class="contact-icon" viewBox="0 0 12 12" aria-label="Telephone"><path d="M2.5 0.5l2 2.4-1.2 1.3c0.6 1.5 1.8 2.8 3.4 3.5l1.3-1.2 2.4 2-1.4 2.5C5.3 10.8 1.2 6.7 0.2 1.8z"/></svg>
      </li>
      <li>+ 94 11 5550183
        <svg class="contact-icon" viewBox="0 0 12 12" aria-label="Fax"><rect x="3" y="0.5" width="6" height="4"/><rect x="0.5" y="5" width="11" height="5" rx="1"/><rect x="3" y="8.5" width="6" height="3"/></svg>
      </li>
      <li>+ 94 77 5550184
        <svg class="contact-icon" viewBox="0 0 12 12" aria-label="Mobile"><path d="M3 0h6a1 1 0 0 1 1 1v10a1 1 0 0 1-1 1H3a1 1 0 0 1-1-1V1a1 1 0 0 1 1-1zm0.5 1.5v7.5h5V1.5z"/></svg>
      </li>
      <li>hello@corvanecolombo.com
        <svg class="contact-icon" viewBox="0 0 12 12" aria-label="Email"><path d="M0 2.5h12v7H0z M0.8 3.2L6 7l5.2-3.8" stroke="#f7f7f7" stroke-width="0.9"/></svg>
      </li>
    </ul>

    <address class="company-address">
      CORVANE LIMITED<br>
      18, Lotus Grove Road<br>
      Colombo 01100, Sri Lanka<br>
      <span class="company-web">www.corvanecolombo.com</span>
    </address>

    <div class="footer-band">
      <span class="band-red"></span>
      <span class="band-dark"></span>
    </div>
  </section>

</body>
</html>
```